Fence & Deck Construction Flyer

My company is called Brackley Fence & Deck and I am seeking a flyer for direct marketing our construction services to residential customers in Calgary. Our focus is home owners aged 35+ that are looking to replace an old fence or deck, although we also do new construction. We use pressure treated wood mainly, but we also use cedar and composite products. You can view our website at www.brackleyfence.ca for some additional insight and pictures of our previous projects. Company colors are black and deep yellow (see website).
The size of the flyer will need to be 6 inches by 11 inches, both sides in full colour.

```html
<!DOCTYPE html>
<html lang="en">
<head>
<meta charset="utf-8">
<title>Brackley Fence &amp; Deck – Flyer Front</title>
<link href="https://fonts.googleapis.com/css2?family=Gelasio:wght@400;700&display=swap" rel="stylesheet">
<style>
:root{
  --stage:#a9a9a9;
  --band:#f3c300;
  --panel-left:#2a2a2a;
  --panel-right:#3b3b3b;
  --ink-dark:#2b2b2b;
  --gold:#f5c400;
  --white:#ffffff;
  --label:#d4d4d4;
  --box:#262626;
  --backdrop-top:#343434;
  --backdrop-bottom:#2c2c2c;
}
*{box-sizing:border-box;margin:0;padding:0}
html,body{width:1200px;height:900px;overflow:hidden}
body{background:var(--stage);font-family:"Gelasio",Georgia,serif;position:relative}
.flyer{position:absolute;left:58px;top:207px;width:1080px;height:571px;background:var(--panel-right);overflow:hidden}
.tagline-band{position:absolute;left:0;top:0;width:52px;height:100%;background:var(--band)}
.tagline{position:absolute;left:26px;top:285px;transform:translate(-50%,-50%) rotate(-90deg);white-space:nowrap;font-weight:700;font-size:21px;color:var(--ink-dark)}
.gallery{position:absolute;left:52px;top:0;width:395px;height:100%;background:var(--panel-left)}
.gallery-label{position:absolute;width:340px;height:35px;background:var(--label);border-radius:5px;text-align:center;font-weight:700;font-size:22px;line-height:38px;color:var(--ink-dark);box-shadow:0 1px 3px rgba(0,0,0,.5)}
.gallery-photo{position:absolute;left:45px;width:296px;height:205px;border:2px solid #e6e6e6}
.photo-fence{background:linear-gradient(180deg,#b9c6cf 0%,#6d5a4a 30%,#b27c52 55%,#4f8a3a 75%,#3f7a2e 100%)}
.photo-deck{background:linear-gradient(180deg,#bcc8d2 0%,#37507a 30%,#2f4a73 50%,#c8a676 72%,#4a8a34 100%)}
.masthead{position:absolute;left:463px;top:11px;width:596px;height:131px;background:var(--box);border:2px solid #f0f0f0;border-radius:8px;box-shadow:0 0 8px rgba(255,255,255,.35)}
.brand{position:absolute;left:12px;top:8px;width:300px;text-align:center;color:var(--gold);font-weight:700;line-height:1.15}
.brand .line1{display:block;font-size:48px}
.brand .line2{display:block;font-size:40px}
.contact{position:absolute;left:318px;top:14px;width:260px;text-align:center;color:var(--white);font-weight:700;font-size:15px;line-height:21px}
.contact .email{display:block;margin-top:16px;margin-bottom:4px}
.contact .phone{color:var(--gold);font-size:23px}
.service{position:absolute;color:var(--white);font-weight:700;font-size:13px;line-height:16px;text-align:justify;hyphens:auto;-webkit-hyphens:auto}
.service .head{color:var(--gold);font-size:17px}
.service .arrow{color:var(--gold);font-size:13px;margin-right:8px}
.svc-fence{left:464px;top:166px;width:282px}
.svc-deck{left:787px;top:166px;width:252px}
.fence-backdrop{position:absolute;left:462px;top:283px;width:605px;height:237px;background:linear-gradient(180deg,var(--backdrop-top),var(--backdrop-bottom));border-radius:4px 4px 0 0}
.svc-replace{left:468px;top:306px;width:570px}
.offer{position:absolute;top:394px;width:276px;height:109px;border:2px solid #eeeeee;border-radius:8px;background:linear-gradient(180deg,#5b5b5b,#3c3c3c);text-align:center;color:var(--gold);font-weight:700;box-shadow:0 0 6px rgba(255,255,255,.3)}
.offer-free{left:477px}
.offer-save{left:770px}
.offer .big{display:block;font-size:44px;line-height:1;margin-top:16px}
.offer-save .big{font-size:27px;margin-top:8px}
.offer-save .big b{font-size:40px}
.offer .small{display:block;font-size:15px;line-height:19px}
.offer-free .small{margin-top:14px}
.offer-save .small{margin-top:6px}
.call-line{position:absolute;left:447px;top:522px;width:633px;text-align:center;color:var(--gold);font-weight:700;font-size:15px}
.call-line .free{font-size:22px}
.call-line .num{font-size:19px}
</style>
</head>
<body>
<main class="flyer">
  <div class="tagline-band"><p class="tagline">“The residential wood fence and deck specialists”</p></div>

  <section class="gallery">
    <h2 class="gallery-label" style="left:23px;top:28px">Wood Fence</h2>
    <div class="gallery-photo photo-fence" style="top:73px" role="img" aria-label="Photo of a newly built cedar wood fence in a grassy backyard"></div>
    <h2 class="gallery-label" style="left:27px;top:306px">Wood Decks</h2>
    <div class="gallery-photo photo-deck" style="top:351px" role="img" aria-label="Photo of a new wood deck with stairs behind a blue house"></div>
  </section>

  <header class="masthead">
    <h1 class="brand"><span class="line1">Brackley</span><span class="line2">Fence &amp; Deck</span></h1>
    <div class="contact">
      <span>482 Maplecrest Way, NW</span><br>
      <span>Calgary, AB T3X 2K9</span>
      <span class="email">brackleyfencedeck@mail.com</span>
      <span>Phone <span class="phone">(403) 555 0148</span></span>
    </div>
  </header>

  <p class="service svc-fence"><span class="arrow">&#10148;</span><span class="head">Wood Fence:</span> Affordable solutions for all of your wood fencing needs. Our quality fencing contractors can design and build the fence that fits your needs and your budget.</p>
  <p class="service svc-deck"><span class="arrow">&#10148;</span><span class="head">Wood Decks:</span> Quality deck contractors at an affordable price. Low cost doesn't have to mean less value, we offer you the best of both worlds. Our deck builders are quick and efficient, while maintaining close attention to detail.</p>

  <div class="fence-backdrop" role="img" aria-label="Dark background illustration of a picket fence"></div>

  <p class="service svc-replace"><span class="arrow">&#10148;</span><span class="head">Replacements and New Projects:</span> We can remove and haul away your old fence or deck if required. In some cases, same day fence replacement service is available upon request.</p>

  <div class="offer offer-free">
    <span class="big">FREE</span>
    <span class="small">on site consultation &amp; quote !</span>
  </div>
  <div class="offer offer-save">
    <span class="big">SAVE <b>$50</b></span>
    <span class="small">on removal and haul away of<br>your old fence &amp; deck !</span>
  </div>

  <p class="call-line">Call us today for a <span class="free">FREE</span> on site consultation and quote - <span class="num">(403) 555-0148</span></p>
</main>
</body>
</html>
```